Business Card Design

New business card design

Target Market(s)

Residential & Commercial Property Managers

Industry/Entity Type

Plumbing Services

Contact Information for Business Card

Name - Tom Brereton, title - Director, Phone Number - 0431 862 517, email - tom@rvk-plumbing.com.au, Company ABN - 73 512 938 204,

Font styles to use
Sans Serif

Colors
0054AA
0677BA
7BADD7
CADEEF
E8F1F8

```html
<!DOCTYPE html>
<html lang="en">
<head>
<meta charset="utf-8">
<title>RVK Plumbing Services – Business Card</title>
<link href="https://fonts.googleapis.com/css2?family=Montserrat:wght@300;400;500;700&display=swap" rel="stylesheet">
<style>
  :root {
    --page-bg: #ecebe8;
    --card-bg: #ffffff;
    --ink: #1e262d;
    --accent: #29a8e0;
    --tagline: #7a6b62;
    --shadow: rgba(0, 0, 0, 0.18);
  }
  * { box-sizing: border-box; margin: 0; padding: 0; }
  html, body {
    width: 1200px; height: 900px; overflow: hidden;
    background: var(--page-bg);
    font-family: "Montserrat", sans-serif;
    color: var(--ink);
  }
  .canvas { position: relative; width: 1200px; height: 900px; }
  .card {
    position: absolute;
    width: 560px; height: 320px;
    background: var(--card-bg);
    border-radius: 30px;
    box-shadow: 0 12px 30px var(--shadow);
    overflow: hidden;
  }
  .card--back { left: 560px; top: 100px; }
  .card--front { left: 80px; top: 470px; }

  .brand-name {
    font-family: "Montserrat", sans-serif;
    font-weight: 300;
    color: var(--ink);
    letter-spacing: 0.02em;
    line-height: 1;
    display: flex; align-items: center; gap: 14px;
  }
  .brand-dot { width: 16px; height: 16px; border-radius: 50%; background: var(--accent); }
  .brand-tagline {
    font-family: "Montserrat", sans-serif;
    font-weight: 300;
    color: var(--tagline);
    letter-spacing: 0.9em;
    text-transform: lowercase;
  }

  /* back side */
  .card--back .brand {
    position: absolute; left: 0; right: 0; top: 92px;
    display: flex; flex-direction: column; align-items: center;
  }
  .card--back .brand-name { font-size: 104px; }
  .card--back .brand-tagline { font-size: 15px; margin-top: 18px; margin-left: 0.9em; }

  /* front side */
  .card--front .brand { position: absolute; left: 42px; top: 24px; }
  .card--front .brand-name { font-size: 74px; }
  .card--front .brand-tagline { font-size: 11px; margin-top: 14px; }

  .drop-mark {
    position: absolute; right: 28px; top: 58px;
    width: 120px; height: 120px; border-radius: 50%;
    background: var(--accent);
  }

  .person { position: absolute; left: 0; top: 160px; padding-left: 34px; }
  .person::before {
    content: ""; position: absolute; left: 0; top: 2px;
    width: 14px; height: 32px; background: var(--accent);
  }
  .person-name { font-weight: 700; font-size: 21px; color: var(--accent); line-height: 1.1; }
  .person-title { font-weight: 400; font-size: 14px; margin-top: 2px; }

  .divider { position: absolute; left: 30px; top: 222px; width: 500px; height: 30px; }

  .contact { position: absolute; left: 30px; top: 252px; list-style: none; }
  .contact li { display: flex; align-items: center; gap: 9px; font-size: 14px; line-height: 22px; }
  .contact svg { width: 14px; height: 14px; flex: none; }

  .abn { position: absolute; right: 30px; bottom: 28px; font-size: 14px; }
</style>
</head>
<body>
<main class="canvas">

  <section class="card card--back" aria-label="Business card back">
    <div class="brand">
      <div class="brand-name">rvk</div>
      <div class="brand-tagline">plumbing services</div>
    </div>
  </section>

  <section class="card card--front" aria-label="Business card front">
    <div class="brand">
      <div class="brand-name">rvk</div>
      <div class="brand-tagline">plumbing services</div>
    </div>

    <div class="drop-mark" aria-hidden="true"></div>

    <div class="person">
      <p class="person-name">Tom Brereton</p>
      <p class="person-title">Director</p>
    </div>

    <svg class="divider" viewBox="0 0 500 30" aria-hidden="true">
      <path d="M0 4 L270 4 C290 4 300 22 320 22 L500 22" fill="none" stroke="var(--accent)" stroke-width="1.6"/>
    </svg>

    <ul class="contact">
      <li>
        <svg viewBox="0 0 24 24" aria-hidden="true"><path d="M6.6 10.8a15.1 15.1 0 0 0 6.6 6.6l2.2-2.2a1 1 0 0 1 1-.25 11.4 11.4 0 0 0 3.6.57 1 1 0 0 1 1 1V20a1 1 0 0 1-1 1A17 17 0 0 1 3 4a1 1 0 0 1 1-1h3.5a1 1 0 0 1 1 1c0 1.25.2 2.45.57 3.57a1 1 0 0 1-.25 1z" fill="var(--accent)"/></svg>
        0431 862 517
      </li>
      <li>
        <svg viewBox="0 0 24 24" aria-hidden="true"><rect x="2" y="5" width="20" height="14" rx="2" fill="none" stroke="var(--accent)" stroke-width="2"/><path d="M3 6l9 7 9-7" fill="none" stroke="var(--accent)" stroke-width="2"/></svg>
        tom@rvk-plumbing.com.au
      </li>
    </ul>

    <p class="abn">Company ABN - 73 512 938 204</p>
  </section>

</main>
</body>
</html>
```